Lanterne architecture business cards

We are a new company based in New Zealand. We Specialize in High end Luxury Residential Architecture.

Every home is bespoke and is designed to each clients individual requirements and needs.

I like to design buildings that inspire people through light and form while offering a high level of comfort and usability.

Lines of sight, proportion and balance are fundamental to the spaces I create.
Updates

August 5th is current deadline - Today's date is the 13th of August.

Target Market(s)

New Zealanders who want a custom individual home design, typically 30-65 year old males and females

Industry/Entity Type

Architecture

Contact Information for Business Card

Director - Derek Tolson
Contact Number - 0279164073
Email - info@lanternearchitecture-example.co.nz
Webstie - www.lanternearchitecture-example.co.nz
Social Media - @lanternearchitecture

Font styles to use
Sans Serif

Requirements
Must have
• Logo (Both Sides)
Website
Email
Contact Number
Social Media

Nice to have
• Texture
Should not have
• More than 3 colours - typically I would've thought 2 would be good to match the logo.

```html
<!DOCTYPE html>
<html lang="en">
<head>
<meta charset="utf-8">
<title>Lanterne architecture business cards</title>
<link href="https://fonts.googleapis.com/css2?family=Lato:wght@300;400;700&display=swap" rel="stylesheet">
<style>
  :root {
    --backdrop: #d9dcda;
    --card-light: #f4f4f2;
    --card-mid: #e7e7e4;
    --card-shade: #dddedb;
    --ink: #141414;
    --ink-soft: #2a2a2a;
    --rule: #3a3a3a;
  }
  * { box-sizing: border-box; margin: 0; padding: 0; }
  html, body {
    width: 1200px;
    height: 900px;
    overflow: hidden;
    background: var(--backdrop);
    font-family: "Lato", sans-serif;
    color: var(--ink);
  }
  .canvas {
    position: relative;
    width: 1200px;
    height: 900px;
  }
  .card {
    position: absolute;
    width: 540px;
    height: 330px;
    background:
      radial-gradient(ellipse at 30% 25%, var(--card-light) 0%, transparent 60%),
      radial-gradient(ellipse at 75% 70%, var(--card-shade) 0%, transparent 55%),
      radial-gradient(ellipse at 60% 20%, var(--card-mid) 0%, transparent 50%),
      var(--card-mid);
    box-shadow: 0 10px 28px rgba(0,0,0,0.12);
  }
  .card--front { left: 80px; top: 110px; }
  .card--back { left: 580px; top: 460px; }

  /* Front */
  .front-brand {
    position: absolute;
    left: 0; right: 0;
    top: 100px;
    text-align: center;
  }
  .brand-dot {
    display: block;
    width: 46px;
    height: 46px;
    margin: 0 auto 26px;
    border: 4px solid var(--ink);
    border-radius: 50%;
  }
  .brand-name {
    font-weight: 300;
    font-size: 22px;
    letter-spacing: 0.42em;
    text-transform: uppercase;
    color: var(--ink);
    padding-left: 0.42em;
  }
  .front-web {
    position: absolute;
    left: 0; right: 0;
    top: 240px;
    text-align: center;
    font-weight: 300;
    font-size: 11px;
    letter-spacing: 0.14em;
    color: var(--ink-soft);
  }
  .front-web::after {
    content: "";
    display: block;
    width: 170px;
    height: 1px;
    margin: 10px auto 0;
    background: var(--rule);
  }

  /* Back */
  .back-brand {
    position: absolute;
    left: 0;
    width: 270px;
    top: 128px;
    text-align: center;
  }
  .back-brand .brand-dot {
    width: 30px;
    height: 30px;
    border-width: 3px;
    margin-bottom: 16px;
  }
  .back-brand .brand-name {
    font-size: 12px;
    letter-spacing: 0.32em;
    padding-left: 0.32em;
  }
  .back-divider {
    position: absolute;
    left: 270px;
    top: 80px;
    width: 1px;
    height: 170px;
    background: var(--rule);
  }
  .contact {
    position: absolute;
    left: 300px;
    top: 92px;
    right: 16px;
  }
  .contact-name {
    font-weight: 700;
    font-size: 14px;
    margin-bottom: 18px;
  }
  .contact-list { list-style: none; }
  .contact-item {
    display: flex;
    align-items: center;
    gap: 7px;
    font-size: 10.5px;
    font-weight: 400;
    color: var(--ink-soft);
    margin-bottom: 11px;
    white-space: nowrap;
  }
  .contact-icon {
    width: 11px;
    height: 11px;
    flex: none;
  }
</style>
</head>
<body>
<main class="canvas">
  <section class="card card--front" aria-label="Business card front">
    <div class="front-brand">
      <span class="brand-dot"></span>
      <p class="brand-name">Lanterne architecture</p>
    </div>
    <p class="front-web">www.lanternearchitecture-example.co.nz</p>
  </section>

  <section class="card card--back" aria-label="Business card back">
    <div class="back-brand">
      <span class="brand-dot"></span>
      <p class="brand-name">Lanterne architecture</p>
    </div>
    <div class="back-divider"></div>
    <div class="contact">
      <p class="contact-name">Derek Tolson (Director)</p>
      <ul class="contact-list">
        <li class="contact-item">
          <svg class="contact-icon" viewBox="0 0 12 12" aria-hidden="true">
            <circle cx="6" cy="6" r="5.3" fill="none" stroke="#141414" stroke-width="1"/>
            <path d="M4 3.2 L5 3 L5.6 4.6 L4.9 5.1 Q5.5 6.6 6.9 7.1 L7.4 6.4 L9 7 L8.8 8 Q6 8.6 4 6 Q3.3 4.6 4 3.2Z" fill="#141414"/>
          </svg>
          0279164073
        </li>
        <li class="contact-item">
          <svg class="contact-icon" viewBox="0 0 12 12" aria-hidden="true">
            <rect x="0.8" y="2.3" width="10.4" height="7.4" fill="none" stroke="#141414" stroke-width="1"/>
            <path d="M0.8 2.3 L6 6.6 L11.2 2.3" fill="none" stroke="#141414" stroke-width="1"/>
          </svg>
          info@lanternearchitecture-example.co.nz
        </li>
        <li class="contact-item">
          <svg class="contact-icon" viewBox="0 0 12 12" aria-hidden="true">
            <circle cx="6" cy="6" r="5.3" fill="none" stroke="#141414" stroke-width="1"/>
          </svg>
          @lanternearchitecture
        </li>
        <li class="contact-item">
          <svg class="contact-icon" viewBox="0 0 12 12" aria-hidden="true">
            <circle cx="6" cy="6" r="5.3" fill="none" stroke="#141414" stroke-width="1"/>
            <ellipse cx="6" cy="6" rx="2.3" ry="5.3" fill="none" stroke="#141414" stroke-width="0.8"/>
            <line x1="0.7" y1="6" x2="11.3" y2="6" stroke="#141414" stroke-width="0.8"/>
          </svg>
          www.lanternearchitecture-example.co.nz
        </li>
      </ul>
    </div>
  </section>
</main>
</body>
</html>
```